Rising Paths Web Design

I am starting a new company that will provide LIFE COACHING services - I have tried to design a website, but it's too complicated. Right now, it's just me - I'm the only person that will provide services through the website - I have used artmarket to purchase a logo (see below). I want to be able to update the website myself, but need a template - basic design. Because I am not technologically savvy enough to explain in words - I basically want to have a website that will provide basic information about my services (coaching), a page about me and my background, hopefully scheduling possibilities, and testimonials — also a page for writing/blogs. I bought a website through NetHarbor - so when I have a template, I guess I”d use that - but maybe I’ll need to work with a designer to actually get it up on the internet. I have a head shot that I’ll upload, too.
Target Market(s)
Clients from the independent (private school) world - teachers, administrators
Number of Pages Required
4 page
Look and feel
Each slider illustrates characteristics of the customer's brand and the style your logo design should communicate.

```html
<!DOCTYPE html>
<html lang="en">
<head>
<meta charset="utf-8">
<title>Rising Paths – Marriage Counselling and Life Coaching</title>
<link rel="stylesheet" href="https://fonts.googleapis.com/css2?family=Cormorant+Garamond:wght@500;600&family=Nunito+Sans:wght@400;600;700&display=swap">
<style>
:root{
  --teal:#17a898;
  --teal-bright:#2ee6c6;
  --mint:#eaf6f3;
  --deep-green:#03594a;
  --grey-bg:#f4f6f7;
  --ink:#1d1d1d;
  --body:#3d3d3d;
  --muted:#6b6b6b;
  --footer:#111313;
  --white:#ffffff;
}
*{box-sizing:border-box;margin:0;padding:0}
html,body{width:1200px;height:3667px;overflow:hidden}
body{position:relative;background:var(--white);font-family:"Nunito Sans",Arial,sans-serif;color:var(--body)}
.abs{position:absolute}
.serif{font-family:"Cormorant Garamond",Georgia,serif;font-weight:500;color:var(--ink)}
.btn{position:absolute;display:flex;align-items:center;gap:8px;background:var(--teal);color:var(--white);font-size:10px;font-weight:700;letter-spacing:0;text-transform:uppercase;padding-left:8px;height:31px;white-space:nowrap;overflow:hidden}
.btn .btn-icon{flex:none;width:17px;height:17px;border-radius:50%;background:var(--white);display:flex;align-items:center;justify-content:center}
.ph{position:absolute}

/* hero */
.hero{position:absolute;left:0;top:0;width:1200px;height:534px}
.hero-bg{position:absolute;left:0;top:0;width:847px;height:534px;background:var(--mint)}
.logo{position:absolute;display:flex;align-items:center;gap:10px;font-family:"Cormorant Garamond",Georgia,serif;font-weight:600;font-size:20px;letter-spacing:.5px;text-transform:uppercase;white-space:nowrap}
.logo .mark{width:16px;height:16px;border-radius:50%;border:2px solid var(--teal)}
.nav-item{position:absolute;top:53px;font-size:11.5px;font-weight:600;color:var(--ink);white-space:nowrap}
.nav-item.active{color:var(--teal)}
.hero-eyebrow{left:130px;top:218px;font-size:13px}
.hero-title{left:130px;top:240px;font-size:41px;line-height:44px}
.hero-text{left:130px;top:351px;width:380px;font-size:13.5px;line-height:19px;color:var(--ink)}

/* about */
.eyebrow{font-size:13px;color:var(--ink)}
.about-title{left:612px;top:650px;font-size:34px;line-height:36px}
.about-text{left:612px;top:755px;width:462px;font-size:13px;line-height:19.3px}
.social{position:absolute;width:34px;height:34px;border-radius:50%;background:#e4f3f0;display:flex;align-items:center;justify-content:center}
.social i{width:18px;height:18px;border-radius:50%;background:var(--teal)}

.feature{position:absolute;width:300px;text-align:center}
.feature .icon{width:64px;height:76px;margin:0 auto;border:2px solid var(--ink);border-radius:6px;background:#f1faf8}
.feature h3{margin-top:22px;font-size:21px}
.feature p{margin-top:12px;font-size:13px;line-height:20px}

/* services */
.services{position:absolute;left:0;top:1311px;width:1200px;height:528px;background:var(--grey-bg)}
.section-title{position:absolute;left:0;width:1200px;text-align:center;font-size:34px}
.section-sub{position:absolute;left:0;width:1200px;text-align:center;font-size:13px;color:var(--ink)}
.service{position:absolute;width:230px;text-align:center}
.service h3{font-size:19px;white-space:nowrap}
.service p{font-size:10.5px;color:var(--muted);margin-top:3px}

/* testimonials */
.testimonials{position:absolute;left:0;top:1839px;width:1200px;height:510px;background:var(--deep-green)}
.testi-title{left:670px;top:1902px;font-size:36px;color:var(--white)}
.testi-text{left:670px;top:2026px;width:400px;font-size:13px;line-height:19px;color:#e3f1ee}
.testi-name{left:732px;top:2139px;font-family:"Cormorant Garamond",Georgia,serif;font-size:14px;color:var(--white);text-transform:uppercase}
.testi-role{left:732px;top:2158px;font-size:8.5px;color:#d4ebe6;text-transform:uppercase}

/* blog */
.post{position:absolute;top:2488px;width:300px}
.post .tag{position:absolute;left:2px;top:38px;width:25px;height:105px;background:var(--teal);color:var(--white);font-size:11px;writing-mode:vertical-rl;transform:rotate(180deg);display:flex;align-items:center;justify-content:center;white-space:nowrap}
.post h3{position:absolute;top:197px;width:300px;font-size:19px;line-height:24px;color:#333}

/* appointment */
.appt{position:absolute;left:0;top:2786px;width:1200px;height:495px;background:linear-gradient(100deg,#3c4446 0%,#5d5a55 35%,#8a7560 60%,#3e3e3a 100%)}
.appt-card{position:absolute;left:239px;top:2868px;width:722px;height:332px;background:#f0f0ef}
.field{position:absolute;border:1px solid #8d8d8d;background:transparent;font-size:9.5px;color:#777;padding:7px 10px}
.submit{position:absolute;left:441px;top:3139px;width:316px;height:30px;background:#23b49f;color:var(--white);font-size:10px;display:flex;align-items:center;justify-content:center;text-transform:uppercase}

/* footer */
.footer{position:absolute;left:0;top:3281px;width:1200px;height:386px;background:var(--footer)}
.foot-title{position:absolute;font-family:"Cormorant Garamond",Georgia,serif;font-weight:500;font-size:20px;color:var(--teal)}
.foot-list{position:absolute;list-style:none;font-size:11.5px;color:#e8e8e8;line-height:24.3px;white-space:nowrap}
.foot-divider{position:absolute;top:3349px;width:1px;height:146px;background:#3a3a3a}
.contact-row{position:absolute;left:873px;display:flex;gap:10px;font-size:11px;color:#e8e8e8;line-height:15px;white-space:nowrap}
.contact-row .ci{flex:none;width:26px;height:26px;border-radius:50%;background:#2a2d2d;display:flex;align-items:center;justify-content:center}
.foot-social{position:absolute;top:3497px;width:31px;height:31px;border-radius:50%;background:var(--teal);display:flex;align-items:center;justify-content:center}
.foot-social i{width:12px;height:12px;border-radius:50%;background:var(--white)}
.copyright{position:absolute;left:0;top:3593px;width:1200px;text-align:center;font-size:11px;color:#e8e8e8}
.copyright span{color:var(--teal)}
</style>
</head>
<body>

<!-- hero -->
<section class="hero">
  <div class="hero-bg"></div>
  <div class="logo" style="left:130px;top:48px;color:#3a3a3a"><span class="mark"></span>Rising Paths</div>
  <nav>
    <span class="nav-item active" style="left:524px">HOME</span>
    <span class="nav-item" style="left:598px">ABOUT ME</span>
    <span class="nav-item" style="left:697px">SERVICES</span>
    <span class="nav-item" style="left:790px">BLOG</span>
    <span class="nav-item" style="left:860px">CONTACT ME</span>
  </nav>
  <div class="btn" style="left:959px;top:44px;width:111px"><span class="btn-icon"><svg width="9" height="9" viewBox="0 0 10 10"><path d="M1 5h7M5 2l3 3-3 3" stroke="#17a898" stroke-width="1.6" fill="none"/></svg></span>Get Schedule</div>
  <p class="abs hero-eyebrow">Finding Balance</p>
  <h1 class="abs serif hero-title">Marriage Counselling<br>and Life Coaching</h1>
  <p class="abs hero-text">But in certain circumstances and owing to the claims of duty or the obligations</p>
  <div class="btn" style="left:131px;top:411px;width:111px"><span class="btn-icon"><svg width="9" height="9" viewBox="0 0 10 10"><path d="M1 5h7M5 2l3 3-3 3" stroke="#17a898" stroke-width="1.6" fill="none"/></svg></span>Get Started</div>
  <div class="ph" role="img" aria-label="Photo of a joyful man and woman jumping in the air, in jeans and white tees" style="left:585px;top:72px;width:470px;height:468px;background:radial-gradient(ellipse at 50% 50%,#dcdcdc 0%,#c9ced3 40%,rgba(234,246,243,0) 72%)"></div>
</section>

<!-- about -->
<svg class="abs" style="left:126px;top:625px" width="410" height="420" viewBox="0 0 410 420">
  <circle cx="204" cy="208" r="199" fill="none" stroke="var(--teal)" stroke-width="2"/>
  <circle cx="208" cy="206" r="192" fill="none" stroke="var(--teal)" stroke-width="1.5"/>
</svg>
<div class="ph" role="img" aria-label="Head shot of the coach, a smiling woman with short blonde hair" style="left:145px;top:648px;width:384px;height:384px;border-radius:50%;background:radial-gradient(circle at 50% 45%,#d9b89c 0%,#b8a48e 35%,#8f8f8a 70%,#c4c6c2 100%)"></div>
<p class="abs eyebrow" style="left:612px;top:628px">About Me</p>
<h2 class="abs serif about-title">Excepteur sint Occaecat<br>&amp; Consulting.</h2>
<p class="abs about-text">At vero eos et accusamus et iusto odio dignissimos ducimus qui blanditiis praesentium voluptatum deleniti atque corrupti quos dolores et quas molestias excepturi sint occaecati cupiditate non provident, similique sunt in culpa qui officia deserunt mollitia animi, id est laborum et dolorum fuga. Et harum quidem rerum facilis est et expedita distinctio.</p>
<div class="btn" style="left:612px;top:887px;width:111px"><span class="btn-icon"><svg width="9" height="9" viewBox="0 0 10 10"><path d="M1 5h7M5 2l3 3-3 3" stroke="#17a898" stroke-width="1.6" fill="none"/></svg></span>About Me</div>
<div class="social" style="left:612px;top:947px"><i></i></div>
<div class="social" style="left:659px;top:947px"><i></i></div>
<div class="social" style="left:706px;top:947px"><i></i></div>
<div class="social" style="left:753px;top:947px"><i></i></div>

<div class="feature" style="left:129px;top:1086px"><div class="icon" role="img" aria-label="Line icon of a book"></div><h3 class="serif">Sspecimen Book</h3><p>Tristique et egestas quis ipsum suspendisse<br>commodo ultrices.</p></div>
<div class="feature" style="left:449px;top:1086px"><div class="icon" role="img" aria-label="Line icon of a coach presenting ideas"></div><h3 class="serif">Latin Literature</h3><p>Tristique et egestas quis ipsum suspendisse<br>commodo ultrices.</p></div>
<div class="feature" style="left:770px;top:1086px"><div class="icon" role="img" aria-label="Line icon of a person with a growth chart"></div><h3 class="serif">Reproduced Below</h3><p>Tristique et egestas quis ipsum suspendisse<br>commodo ultrices.</p></div>

<!-- services -->
<section class="services"></section>
<h2 class="serif section-title" style="top:1362px">Our Services</h2>
<p class="section-sub" style="top:1415px">Lorem ipsum dolor sit amet mollis felis dapibus arcu donec viverra.</p>

<svg class="abs" style="left:0;top:1470px" width="1200" height="220" viewBox="0 0 1200 220">
  <g fill="none" stroke="var(--teal)" stroke-width="1.6">
    <circle cx="235" cy="110" r="104"/><circle cx="475" cy="110" r="104"/><circle cx="715" cy="110" r="104"/><circle cx="955" cy="110" r="104"/>
  </g>
</svg>
<div class="ph" role="img" aria-label="Photo of a smiling coach at a desk" style="left:145px;top:1490px;width:178px;height:178px;border-radius:50%;background:linear-gradient(135deg,#c9b8a6,#e9e4dd 60%,#8d7f70)"></div>
<div class="ph" role="img" aria-label="Photo of a woman holding a self-love note" style="left:385px;top:1490px;width:178px;height:178px;border-radius:50%;background:linear-gradient(135deg,#b8a692,#ece6dd 60%,#9a8775)"></div>
<div class="ph" role="img" aria-label="Photo of two women in a coaching session" style="left:625px;top:1490px;width:178px;height:178px;border-radius:50%;background:linear-gradient(135deg,#c7a27e,#e6d7c4 55%,#8c6a4e)"></div>
<div class="ph" role="img" aria-label="Photo of a coach speaking with a client" style="left:865px;top:1490px;width:178px;height:178px;border-radius:50%;background:linear-gradient(135deg,#a89a8c,#d9d3cb 55%,#5e5852)"></div>

<div class="service" style="left:120px;top:1690px"><h3 class="serif">Morbi Blandit Cursus Risus</h3><p>On the other hand denounce</p></div>
<div class="service" style="left:360px;top:1690px"><h3 class="serif">Morbi Blandit Cursus Risus</h3><p>On the other hand denounce</p></div>
<div class="service" style="left:600px;top:1690px"><h3 class="serif">Morbi Blandit Cursus Risus</h3><p>On the other hand denounce</p></div>
<div class="service" style="left:840px;top:1690px"><h3 class="serif">Morbi Blandit Cursus Risus</h3><p>On the other hand denounce</p></div>
<div class="btn" style="left:185px;top:1752px;width:110px"><span class="btn-icon"><svg width="9" height="9" viewBox="0 0 10 10"><path d="M1 5h7M5 2l3 3-3 3" stroke="#17a898" stroke-width="1.6" fill="none"/></svg></span>View Details</div>
<div class="btn" style="left:425px;top:1752px;width:110px"><span class="btn-icon"><svg width="9" height="9" viewBox="0 0 10 10"><path d="M1 5h7M5 2l3 3-3 3" stroke="#17a898" stroke-width="1.6" fill="none"/></svg></span>View Details</div>
<div class="btn" style="left:665px;top:1752px;width:110px"><span class="btn-icon"><svg width="9" height="9" viewBox="0 0 10 10"><path d="M1 5h7M5 2l3 3-3 3" stroke="#17a898" stroke-width="1.6" fill="none"/></svg></span>View Details</div>
<div class="btn" style="left:905px;top:1752px;width:110px"><span class="btn-icon"><svg width="9" height="9" viewBox="0 0 10 10"><path d="M1 5h7M5 2l3 3-3 3" stroke="#17a898" stroke-width="1.6" fill="none"/></svg></span>View Details</div>

<!-- testimonials -->
<section class="testimonials"></section>
<div class="ph" role="img" aria-label="Photo of a smiling young woman with red hair in an office" style="left:140px;top:1870px;width:450px;height:425px;border-radius:50%;background:linear-gradient(120deg,#5f7a52 0%,#c9c3b8 40%,#e8d3c0 60%,#8fa8b8 100%)"></div>
<svg class="abs" style="left:125px;top:1855px" width="480" height="460" viewBox="0 0 480 460">
  <path d="M404 390 A226 214 0 1 0 348 426 L415 446 Z" fill="none" stroke="var(--teal-bright)" stroke-width="7" stroke-linejoin="round"/>
</svg>
<div class="ph" role="img" aria-label="Small photo of a bearded client" style="left:130px;top:1872px;width:50px;height:50px;border-radius:50%;border:2px solid #fff;background:linear-gradient(135deg,#c9a88c,#6d5a4a)"></div>
<div class="ph" role="img" aria-label="Small photo of a client in a suit" style="left:130px;top:2270px;width:50px;height:50px;border-radius:50%;border:2px solid #fff;background:linear-gradient(135deg,#d1b7a0,#3d3a38)"></div>
<h2 class="abs serif testi-title">Testimonials</h2>
<svg class="abs" style="left:670px;top:1972px" width="44" height="34" viewBox="0 0 44 34"><g fill="#fff"><path d="M2 2h16v16l-8 14H3l6-14H2z"/><path d="M24 2h16v16l-8 14h-7l6-14h-7z"/></g></svg>
<p class="abs testi-text">On the other hand, we denounce with righteous indignation and dislike men who are so beguiled and demoralized by the charms of pleasure of the moment, so blinded by desire, that they cannot foresee the pain and trouble that are bound.</p>
<div class="ph" role="img" aria-label="Small portrait of the reviewer" style="left:671px;top:2130px;width:48px;height:48px;border-radius:50%;background:linear-gradient(135deg,#c8ab93,#7a6656)"></div>
<p class="abs testi-name">Daniel Prior</p>
<p class="abs testi-role">Co-Founder &amp; CEO, Northwind.co</p>
<div class="abs" style="left:670px;top:2226px;width:20px;height:3px;background:var(--teal-bright)"></div>
<div class="abs" style="left:694px;top:2226px;width:20px;height:3px;background:var(--teal)"></div>
<div class="abs" style="left:718px;top:2226px;width:20px;height:3px;background:#1a7f6e"></div>

<!-- blog -->
<h2 class="serif section-title" style="top:2400px">Recent Blog</h2>
<p class="section-sub" style="top:2448px">Lorem ipsum dolor sit amet mollis felis dapibus arcu donec viverra.</p>
<article class="post" style="left:130px">
  <div class="ph" role="img" aria-label="Photo of a presenter showing charts to a team in a meeting room" style="left:0;top:0;width:300px;height:183px;background:linear-gradient(160deg,#2c2f33 0%,#4a5a6a 40%,#bcc6cf 70%,#e9e9e9 100%)"></div>
  <div class="tag">12th June, 2022</div>
  <h3 class="serif">But who has any right to find fault with a man who chooses</h3>
</article>
<article class="post" style="left:450px">
  <div class="ph" role="img" aria-label="Photo of a smiling grey-haired woman during a session" style="left:0;top:0;width:300px;height:183px;background:linear-gradient(100deg,#cfd2d4 0%,#e9e7e3 45%,#d9b48e 75%,#b78d63 100%)"></div>
  <div class="tag">12th June, 2022</div>
  <h3 class="serif">But who has any right to find fault with a man who chooses</h3>
</article>
<article class="post" style="left:770px">
  <div class="ph" role="img" aria-label="Photo of two women talking over a laptop at a table" style="left:0;top:0;width:300px;height:183px;background:linear-gradient(120deg,#4b4a46 0%,#a7a29a 40%,#e6e3de 70%,#c7c1b8 100%)"></div>
  <div class="tag">12th June, 2022</div>
  <h3 class="serif">But who has any right to find fault with a man who chooses</h3>
</article>

<!-- appointment -->
<section class="appt" role="img" aria-label="Background photo of two friends cheering at sunset"></section>
<div class="appt-card"></div>
<p class="abs" style="left:239px;top:2896px;width:722px;text-align:center;font-size:13.5px;color:var(--ink)">Request Appointment</p>
<h2 class="abs serif" style="left:239px;top:2916px;width:722px;text-align:center;font-size:25px">Make an Appointment With Me</h2>
<div class="field" style="left:279px;top:2974px;width:315px;height:30px">Name:</div>
<div class="field" style="left:607px;top:2974px;width:315px;height:30px">Email:</div>
<div class="field" style="left:279px;top:3015px;width:315px;height:30px">Phone:</div>
<div class="field" style="left:607px;top:3015px;width:315px;height:30px">Choose Date:</div>
<div class="field" style="left:279px;top:3056px;width:643px;height:70px">Message:</div>
<div class="submit">Submit</div>

<!-- footer -->
<footer class="footer"></footer>
<div class="logo" style="left:132px;top:3397px;color:#fff;font-size:21px"><span class="mark"></span>Rising Paths</div>
<div class="foot-social" style="left:130px"><i></i></div>
<div class="foot-social" style="left:170px"><i></i></div>
<div class="foot-social" style="left:211px"><i></i></div>
<div class="foot-social" style="left:251px"><i></i></div>

<h4 class="foot-title" style="left:450px;top:3334px">Sitemap</h4>
<ul class="foot-list" style="left:450px;top:3370px"><li>Home</li><li>About Me</li><li>Services</li><li>Blog</li><li>Contact Me</li></ul>
<div class="foot-divider" style="left:576px"></div>
<h4 class="foot-title" style="left:643px;top:3334px">Coaching</h4>
<ul class="foot-list" style="left:643px;top:3370px"><li>Similique Qunt</li><li>Maiores Alias</li><li>Bound to Ensue</li><li>Choice is Untrammelled</li><li>Saepe Eveniet</li></ul>
<div class="foot-divider" style="left:820px"></div>
<h4 class="foot-title" style="left:873px;top:3334px">Contact Me</h4>
<div class="contact-row" style="top:3374px"><span class="ci"><svg width="12" height="14" viewBox="0 0 12 14"><path d="M6 13s5-5 5-8A5 5 0 0 0 1 5c0 3 5 8 5 8z" fill="#fff"/><circle cx="6" cy="5" r="1.8" fill="#2a2d2d"/></svg></span><span>27/B Lorem ipsum dolar sit amet<br>Harlow 41MP UKE</span></div>
<div class="contact-row" style="top:3427px;align-items:center"><span class="ci"><svg width="12" height="12" viewBox="0 0 12 12"><path d="M2 1h3l1 3-2 1a7 7 0 0 0 3 3l1-2 3 1v3c0 1-1 1-2 1A10 10 0 0 1 1 3c0-1 0-2 1-2z" fill="#fff"/></svg></span><span>+2 (555) 240 7730</span></div>
<div class="contact-row" style="top:3467px;align-items:center"><span class="ci"><svg width="12" height="10" viewBox="0 0 12 10"><rect x="0.5" y="0.5" width="11" height="9" fill="#fff"/><path d="M1 1l5 4 5-4" stroke="#2a2d2d" fill="none"/></svg></span><span>hello@risingpaths.com</span></div>

<p class="copyright">Copyright © 2022 <span>Rising Paths Coaching</span>. All Rights Reserved.</p>

</body>
</html>
```